Business card design for Plumbing and Gas fitting company

We need a business card design for our plumbing and gas fitting company using the company logo and director details. Design should be modern and eye-catching however kept reasonably simple. This design should be targeted at commercial businesses/work so professionalism is key.

Target Market(s)

Commercial/business

Industry/Entity Type

Plumbing

Contact Information for Business Card

Warren Dohey
Director
027 581 9043
warren@vantorplumbingandgas.example
PO Box 7816
Palmerston North 4472

Font styles to use
Sans Serif

Requirements
Must have
• Logo
• Modern
• Kept simple
Nice to have
• Colour scheme based around logo

```html
<!DOCTYPE html>
<html lang="en">
<head>
<meta charset="utf-8">
<title>Vantor Plumbing &amp; Gas – Business Card</title>
<link href="https://fonts.googleapis.com/css2?family=Oswald:wght@500;700&family=Roboto+Condensed:wght@400;700&display=swap" rel="stylesheet">
<style>
  :root {
    --backdrop: #ededed;
    --card-dark: #050505;
    --card-light: #ffffff;
    --brand-blue: #1a73c2;
    --brand-orange: #ec7a30;
    --text-light: #f2f2f2;
    --text-muted: #9a9a9a;
    --shadow: rgba(0, 0, 0, 0.18);
  }
  * { margin: 0; padding: 0; box-sizing: border-box; }
  html, body {
    width: 1200px;
    height: 800px;
    overflow: hidden;
    background: var(--backdrop);
  }
  .canvas {
    position: relative;
    width: 1200px;
    height: 800px;
  }
  .card {
    position: absolute;
    width: 540px;
    height: 309px;
    border-radius: 3px;
    overflow: hidden;
    box-shadow: 0 6px 18px var(--shadow);
  }
  .card--back {
    left: 50px;
    top: 140px;
    background: var(--card-dark);
    color: var(--text-light);
  }
  .card--front {
    left: 610px;
    top: 350px;
    background: var(--card-light);
  }
  .corner-accent {
    position: absolute;
    top: 0;
    right: 0;
    width: 540px;
    height: 309px;
    pointer-events: none;
  }
  .corner-accent__band { fill: var(--brand-blue); }
  .corner-accent__tip { fill: var(--brand-orange); }
  .person {
    position: absolute;
    left: 44px;
    top: 52px;
    padding-left: 12px;
    border-left: 3px solid var(--brand-blue);
  }
  .person__name {
    font-family: "Oswald", sans-serif;
    font-weight: 700;
    font-size: 26px;
    letter-spacing: 0.5px;
    text-transform: uppercase;
    color: #d9d9d9;
    line-height: 1.05;
  }
  .person__role {
    font-family: "Roboto Condensed", sans-serif;
    font-size: 14px;
    color: var(--text-muted);
    margin-top: 2px;
  }
  .contact {
    position: absolute;
    left: 100px;
    top: 168px;
    font-family: "Roboto Condensed", sans-serif;
    font-size: 17px;
    line-height: 1.3;
    border-collapse: collapse;
  }
  .contact th {
    font-weight: 700;
    text-align: left;
    vertical-align: top;
    padding-right: 12px;
  }
  .contact td { font-weight: 400; }
  .brand {
    position: absolute;
    left: 0;
    right: 0;
    top: 50%;
    transform: translateY(-50%);
    display: flex;
    align-items: center;
    justify-content: center;
    gap: 12px;
  }
  .brand__dot {
    width: 22px;
    height: 22px;
    border-radius: 50%;
    background: var(--brand-orange);
  }
  .brand__name {
    font-family: "Roboto Condensed", sans-serif;
    font-weight: 700;
    font-size: 34px;
    color: var(--brand-blue);
  }
</style>
</head>
<body>
<main class="canvas">
  <section class="card card--back" aria-label="Business card back">
    <svg class="corner-accent" viewBox="0 0 540 309" aria-hidden="true">
      <polygon class="corner-accent__band" points="385,0 428,0 540,112 540,155"/>
      <polygon class="corner-accent__band" points="448,0 486,0 540,54 540,92"/>
      <polygon class="corner-accent__tip" points="500,0 540,0 540,40"/>
    </svg>
    <div class="person">
      <p class="person__name">Warren Dohey</p>
      <p class="person__role">Director</p>
    </div>
    <table class="contact">
      <tr><th>P:</th><td>027 581 9043</td></tr>
      <tr><th>M:</th><td>warren@vantorplumbingandgas.example</td></tr>
      <tr><th>A:</th><td>PO Box 7816<br>Palmerston North 4472</td></tr>
    </table>
  </section>

  <section class="card card--front" aria-label="Business card front">
    <div class="brand">
      <span class="brand__dot"></span>
      <span class="brand__name">Vantor Plumbing &amp; Gas</span>
    </div>
  </section>
</main>
</body>
</html>
```